Flyer Design for PickUp and Delivery -- 1

I need some graphic design.
Flyer for an upstart business.
Laundry Service: - Dry Cleaning - Fluff and fold - Wash and press.
Laundry Pick-up and Delivery. Its like Zolt but for laundry.
- No picture of a girl holding a laundry basket please.
Include Phone #
Email
Website

here are some inspiration
Check out Sudsy Cubby -- Sudsycubbyx.com

http://www.pagemintery.com/Downloads/PDF/Preview/KT4471902X-PREVIEW.pdf

http://www.tidyleafletz.com/flyers/laundry-flyer.html

http://www.snapvaultimg.com/similar-583920114/stock-vector-laundry-service-flyer-poster-template.html?page=1&inline=402719385

http://www.wellnourmag.com/eco/eco-home/clean-up-your-laundry-habits

```html
<!DOCTYPE html>
<html lang="en">
<head>
<meta charset="utf-8">
<title>Laundry PickUp and Delivery</title>
<link rel="stylesheet" href="https://fonts.googleapis.com/css2?family=Montserrat:ital,wght@0,300;0,600;0,700;1,700&display=swap">
<style>
  :root {
    --sky: #00bef2;
    --ink-grey: #7f7f7f;
    --paper: #ffffff;
  }
  * { margin: 0; padding: 0; box-sizing: border-box; }
  html, body { width: 928px; height: 1200px; overflow: hidden; background: var(--paper); }
  .flyer {
    position: relative; width: 928px; height: 1200px; overflow: hidden;
    background: var(--paper); font-family: "Montserrat", Arial, sans-serif;
  }
  .flyer > * { position: absolute; }
  .top-wave, .title-rule { left: 0; top: 0; }
  .headline {
    left: 0; width: 928px; text-align: center; color: var(--sky);
    font-weight: 700; white-space: nowrap; line-height: 1;
  }
  .headline--main { top: 157px; font-size: 117px; letter-spacing: 1px; }
  .headline--sub { top: 294px; font-size: 80px; letter-spacing: 0.5px; }
  .services-title {
    left: 35px; top: 452px; color: var(--sky);
    font-size: 40px; font-weight: 700; font-style: italic; white-space: nowrap;
  }
  .services-list {
    left: 34px; top: 503px; color: var(--sky); font-size: 30.2px;
    font-weight: 300; white-space: nowrap; letter-spacing: 0.2px;
  }
  .garments {
    left: 206px; top: 566px; width: 532px; height: 260px;
    background: linear-gradient(90deg, #858585, #7a7a7a 50%, #858585);
    border-radius: 18px 18px 4px 4px;
  }
  .washer {
    left: 20px; top: 857px; width: 288px; height: 343px;
    background: var(--sky); border-radius: 8px 8px 0 0;
  }
  .contact { left: 410px; width: 518px; height: 64px; display: flex; align-items: center; }
  .contact svg { flex: none; }
  .contact-text {
    margin-left: 10px; color: var(--ink-grey); font-weight: 700;
    font-style: italic; white-space: nowrap;
  }
  .contact--phone { top: 906px; }
  .contact--phone .contact-text { font-size: 35px; letter-spacing: 0.5px; }
  .contact--email { top: 985px; }
  .contact--web { top: 1058px; }
  .contact--email .contact-text { font-size: 18.5px; }
  .contact--web .contact-text { font-size: 19.5px; }
</style>
</head>
<body>
<main class="flyer">
  <svg class="top-wave" width="928" height="140" viewBox="0 0 928 140" aria-hidden="true">
    <path d="M0 0 H928 V84 C700 100 420 130 210 138 C130 140 60 139 0 135 Z" fill="var(--sky)"/>
  </svg>

  <h1 class="headline headline--main">Laundry</h1>
  <p class="headline headline--sub">PickUp and Delivery</p>

  <svg class="title-rule" width="928" height="450" viewBox="0 0 928 450" aria-hidden="true">
    <path d="M362 417 C560 414 760 418 928 424 V442 C760 428 560 420 362 417 Z" fill="var(--sky)"/>
  </svg>

  <h2 class="services-title">Laundry Services:</h2>
  <p class="services-list">DRY CLEANING - FLUFF AND FOLD - WASH AND PRESS</p>

  <div class="garments" role="img" aria-label="Three grey jacket silhouettes hanging on hangers"></div>

  <div class="washer" role="img" aria-label="Blue washing machine illustration with water in the drum"></div>

  <div class="contact contact--phone">
    <svg width="64" height="64" viewBox="0 0 64 64" aria-hidden="true">
      <circle cx="32" cy="32" r="29" fill="none" stroke="var(--ink-grey)" stroke-width="3"/>
      <path d="M23 18 l6 -1 l4 9 l-4 3 c2 5 5 8 10 10 l3 -4 l9 4 l-1 6 c-1 2 -3 3 -6 3 c-12 -2 -21 -11 -23 -23 c0 -3 1 -5 2 -7 z"
            fill="var(--ink-grey)"/>
    </svg>
    <span class="contact-text">555- 018-274</span>
  </div>

  <div class="contact contact--email">
    <svg width="64" height="64" viewBox="0 0 64 64" aria-hidden="true">
      <circle cx="32" cy="32" r="29" fill="none" stroke="var(--ink-grey)" stroke-width="3"/>
      <text x="32" y="44" text-anchor="middle" font-family="Montserrat, Arial, sans-serif" font-size="34" font-weight="600" fill="var(--ink-grey)">@</text>
    </svg>
    <span class="contact-text">laundrypickupanddelivery@foldmail.com</span>
  </div>

  <div class="contact contact--web">
    <svg width="64" height="64" viewBox="0 0 64 64" aria-hidden="true">
      <circle cx="32" cy="32" r="30" fill="var(--ink-grey)"/>
      <g fill="none" stroke="var(--paper)" stroke-width="2.2">
        <circle cx="32" cy="32" r="17"/>
        <ellipse cx="32" cy="32" rx="7" ry="17"/>
        <line x1="15" y1="32" x2="49" y2="32"/>
        <line x1="32" y1="15" x2="32" y2="49"/>
        <path d="M18 23 H46 M18 41 H46"/>
      </g>
    </svg>
    <span class="contact-text">www.laundrypickupanddeliverz.com</span>
  </div>
</main>
</body>
</html>
```